Varnell Skyworks Limited

Started a consulting business 12 months ago and have since moved location and have grown and seek to identify my self to the industry.
Specializing in quality solutions, business documentation and maintenance solution's

Industry/Entity Type

Business

```html
<!DOCTYPE html>
<html lang="en">
<head>
<meta charset="utf-8">
<title>Varnell Skyworks Limited – Business Card</title>
<link href="https://fonts.googleapis.com/css2?family=Exo+2:wght@400;500;600&display=swap" rel="stylesheet">
<style>
  :root {
    --page-bg: #e4e4e4;
    --card-light: #ffffff;
    --card-shade: #e9e9e9;
    --ink: #1f1f1f;
    --ink-soft: #3a3a3a;
    --band-dark: #232323;
    --accent-green: #9acd32;
    --divider: #2b2b2b;
  }
  html, body {
    margin: 0;
    width: 1200px;
    height: 899px;
    overflow: hidden;
    background: var(--page-bg);
    font-family: "Exo 2", sans-serif;
  }
  .business-card {
    position: absolute;
    left: 120px;
    top: 175px;
    width: 960px;
    height: 548px;
    border-radius: 48px;
    overflow: hidden;
    background: linear-gradient(135deg, var(--card-shade) 0%, var(--card-light) 45%, var(--card-shade) 100%);
    box-shadow: 0 10px 30px rgba(0,0,0,0.18);
  }
  .card-waves {
    position: absolute;
    inset: 0;
  }
  .company-name {
    position: absolute;
    left: 56px;
    top: 178px;
    width: 470px;
    margin: 0;
    font-size: 36px;
    font-weight: 500;
    line-height: 1.2;
    color: var(--ink);
    letter-spacing: 0.3px;
    white-space: nowrap;
  }
  .column-divider {
    position: absolute;
    left: 545px;
    top: 78px;
    width: 2px;
    height: 300px;
    background: var(--divider);
  }
  .contact-block {
    position: absolute;
    left: 572px;
    top: 90px;
    width: 360px;
    color: var(--ink);
  }
  .person-name {
    margin: 0;
    font-size: 22px;
    font-weight: 500;
    letter-spacing: 2px;
  }
  .person-title {
    margin: 2px 0 0;
    font-size: 19px;
    color: var(--ink-soft);
  }
  .office-address {
    margin: 42px 0 0;
    font-size: 20px;
    line-height: 1.3;
    font-style: normal;
    color: var(--ink-soft);
  }
  .contact-list {
    list-style: none;
    margin: 30px 0 0;
    padding: 0;
    font-size: 15px;
    color: var(--ink-soft);
  }
  .contact-list li {
    display: flex;
    align-items: center;
    height: 27px;
  }
  .contact-icon {
    width: 16px;
    height: 16px;
    margin-right: 12px;
    fill: var(--ink);
  }
</style>
</head>
<body>
  <div class="business-card">
    <svg class="card-waves" viewBox="0 0 960 548" preserveAspectRatio="none" aria-hidden="true">
      <path d="M0,300 C180,380 420,462 960,470 L960,548 L0,548 Z" fill="var(--band-dark)"/>
      <path d="M110,318 C320,420 620,455 960,440 L960,456 C620,472 320,440 110,318 Z" fill="var(--accent-green)"/>
    </svg>

    <h1 class="company-name">Varnell Skyworks Limited</h1>

    <div class="column-divider"></div>

    <div class="contact-block">
      <p class="person-name">MARCUS ELLERY</p>
      <p class="person-title">Managing Director</p>
      <address class="office-address">071.12th floor,Harbor Crest<br>Road NWK</address>
      <ul class="contact-list">
        <li>
          <svg class="contact-icon" viewBox="0 0 16 16"><path d="M3.5 1 L6 1.5 L7 5 L5.3 6.3 C6.2 8.2 7.8 9.8 9.7 10.7 L11 9 L14.5 10 L15 12.5 C15 13.9 13.9 15 12.5 15 C6.7 15 1 9.3 1 3.5 C1 2.1 2.1 1 3.5 1 Z"/></svg>
          014 552 8731
        </li>
        <li>
          <svg class="contact-icon" viewBox="0 0 16 16"><path d="M4.5 0.5 H11.5 A1 1 0 0 1 12.5 1.5 V14.5 A1 1 0 0 1 11.5 15.5 H4.5 A1 1 0 0 1 3.5 14.5 V1.5 A1 1 0 0 1 4.5 0.5 Z M5 2.5 V12 H11 V2.5 Z M7.2 13 H8.8 V14.3 H7.2 Z"/></svg>
          014 552 8732
        </li>
        <li>
          <svg class="contact-icon" viewBox="0 0 16 16"><path d="M4 1 H11 V5 H13.5 A1 1 0 0 1 14.5 6 V14 A1 1 0 0 1 13.5 15 H2.5 A1 1 0 0 1 1.5 14 V6 A1 1 0 0 1 2.5 5 H4 Z M5 2 V7 H10 V2 Z M4 9 H6 V10.5 H4 Z M7 9 H9 V10.5 H7 Z M10 9 H12 V10.5 H10 Z M4 11.5 H6 V13 H4 Z M7 11.5 H9 V13 H7 Z M10 11.5 H12 V13 H10 Z"/></svg>
          014 552 8733
        </li>
        <li>
          <svg class="contact-icon" viewBox="0 0 16 16"><path d="M1 3 H15 V13 H1 Z M2.3 4.2 L8 8.6 L13.7 4.2 Z"/></svg>
          hello@varnellsky.com
        </li>
        <li>
          <svg class="contact-icon" viewBox="0 0 16 16"><path d="M8 1 A7 7 0 1 0 8.01 1 Z M8 2.3 C9.1 3.4 9.8 5.3 9.9 7.3 H6.1 C6.2 5.3 6.9 3.4 8 2.3 Z M2.4 8.7 H4.8 C4.9 10.5 5.4 12.2 6.1 13.4 C4.1 12.8 2.7 11 2.4 8.7 Z M2.4 7.3 C2.7 5 4.1 3.2 6.1 2.6 C5.4 3.8 4.9 5.5 4.8 7.3 Z M6.1 8.7 H9.9 C9.8 10.7 9.1 12.6 8 13.7 C6.9 12.6 6.2 10.7 6.1 8.7 Z M11.2 8.7 H13.6 C13.3 11 11.9 12.8 9.9 13.4 C10.6 12.2 11.1 10.5 11.2 8.7 Z M11.2 7.3 C11.1 5.5 10.6 3.8 9.9 2.6 C11.9 3.2 13.3 5 13.6 7.3 Z"/></svg>
          www.varnellskyworks.com
        </li>
      </ul>
    </div>
  </div>
</body>
</html>
```